Custom unique Stationary design for Logistics company

We need a custom, unique , elegant and luxurious full stationary design using our new logo, following these guidelines:
1- Business card: double sided, both sides uses the navy blue as the background main color (same as the code of the navy blue used in our logo).
2- envelope and folder: also use the same navy blue as the main background color.
3- book cover( notepad cover) : same thing with the navy blue
4- letterhead: feel free to use the combination of the colors in our logo.
5- rest of the items are up to your creativity

Target Market(s)

corporates and other businesses

Industry/Entity Type

Logistics and heavy machines contractors

Requirements
Must have
• Letterhead, business card, envelope, notepad cover, paper, file
Nice to have
• navy blue to be main background color for business card, envelope, notepad cover

```html
<!DOCTYPE html>
<html lang="en">
<head>
<meta charset="utf-8">
<title>KRV Stationery Set</title>
<link href="https://fonts.googleapis.com/css2?family=Montserrat:wght@400;600;800&display=swap" rel="stylesheet">
<style>
:root{
  --navy:#1b5276;
  --navy-deep:#164563;
  --navy-faint:#21608a;
  --orange:#e8562a;
  --paper:#ffffff;
  --ink:#555b61;
  --bg:#9a9a9a;
  --rule:#d4d8dc;
}
*{box-sizing:border-box;margin:0;padding:0}
html,body{width:724px;height:1200px;overflow:hidden}
body{background:var(--bg);font-family:"Montserrat",Arial,sans-serif;position:relative;color:var(--ink)}
.piece{position:absolute;background:var(--paper);overflow:hidden;box-shadow:0 1px 3px rgba(0,0,0,.25)}
.wave{position:absolute;left:0;top:0;width:100%;display:block}
.brand{font-family:"Montserrat",Arial,sans-serif;font-weight:800;color:var(--navy);letter-spacing:1px;line-height:1}
.tagline{font-size:4px;letter-spacing:.6px;color:var(--navy);margin-top:2px;text-transform:uppercase}
.tiny{font-size:4.2px;line-height:1.55}
.contact-white{position:absolute;right:12px;top:8px;text-align:right;color:#fff;font-size:4px;line-height:1.6}

/* business cards */
.card-front{left:108px;top:29px;width:242px;height:145px}
.card-front .brand-block{position:absolute;left:18px;top:42px}
.card-front .brand{font-size:30px}
.card-front .name{position:absolute;right:14px;top:8px;text-align:right;color:var(--orange);font-size:7px;font-weight:600}
.card-front .role{display:block;color:#fff;font-size:4.5px;font-weight:400;margin-top:2px}
.card-front .lines{position:absolute;left:18px;top:92px}
.card-front .lines li{list-style:none;display:flex;align-items:center;gap:4px;font-size:4.5px;line-height:2}
.dot{width:4px;height:4px;border-radius:50%;background:var(--orange);display:inline-block}
.card-front .address{position:absolute;right:14px;top:100px;text-align:right;font-size:4.5px;line-height:1.6}
.card-front .base{position:absolute;left:0;bottom:0;width:100%;height:4px;background:var(--navy)}
.card-back{left:374px;top:29px;width:242px;height:145px;background:var(--navy)}
.card-back .brand{position:absolute;left:50%;top:50%;transform:translate(-50%,-50%);font-size:34px;color:var(--navy-deep)}

/* letterheads */
.letterhead{top:193px;width:326px;height:458px}
.letterhead.first{left:29px}
.letterhead.second{left:373px}
.letterhead .brand-block{position:absolute;left:22px;top:48px}
.letterhead .brand{font-size:22px}
.letter-body{position:absolute;left:22px;top:100px;width:276px}
.letter-body .salutation{font-size:6px;color:#333;margin-bottom:10px}
.letter-body p{margin-bottom:7px}
.signature{width:40px;height:10px;margin:8px 0 6px}
.ruled{position:absolute;left:22px;right:22px;top:100px;bottom:30px;
  background:repeating-linear-gradient(to bottom,transparent 0 11px,var(--rule) 11px 12px)}

/* folder open */
.folder-open{left:29px;top:670px;width:326px;height:246px;background:var(--paper)}
.folder-open .panel-left{position:absolute;left:0;top:0;width:50%;height:100%;background:var(--navy)}
.folder-open .panel-left .brand{position:absolute;left:16px;top:80px;font-size:46px;color:var(--navy-faint)}
.folder-open .sheet{position:absolute;left:178px;top:40px;width:132px}
.folder-open .sheet .tiny{font-size:3.4px}
.folder-open .fold{position:absolute;left:50%;top:0;width:1px;height:100%;background:rgba(0,0,0,.15)}

/* folder closed */
.folder-closed{left:29px;top:928px;width:326px;height:253px}
.folder-closed .insert{position:absolute;left:110px;top:14px;width:112px;height:110px;background:#fff;border:1px solid #e2e2e2;overflow:hidden}
.folder-closed .insert .brand{position:absolute;left:8px;top:20px;font-size:10px}
.folder-closed .insert .tiny{position:absolute;left:8px;top:40px;right:8px;font-size:3px}

/* envelopes */
.envelope{left:369px;width:330px}
.env-front{top:670px;height:125px}
.env-front .brand-block{position:absolute;left:50%;top:48px;transform:translateX(-50%);text-align:center}
.env-front .brand{font-size:22px}
.env-back{top:827px;height:125px}
.env-back-navy{top:976px;height:133px;background:var(--navy)}
.flap{position:absolute;inset:0;width:100%;height:100%}
.env-back .brand,.env-back-navy .brand{position:absolute;left:50%;top:54px;transform:translateX(-50%);font-size:20px}
.env-back-navy .brand{color:#fff}
</style>
</head>
<body>

<!-- business card front -->
<section class="piece card-front" aria-label="Business card front">
  <svg class="wave" viewBox="0 0 242 40" preserveAspectRatio="none" height="40">
    <path d="M0 0H242V36C170 26 90 8 0 14Z" fill="var(--navy)"/>
    <path d="M0 18C90 12 170 30 242 40" stroke="var(--orange)" stroke-width="2" fill="none"/>
  </svg>
  <div class="name">Daniel Reyes<span class="role">Operations Manager</span></div>
  <div class="brand-block"><div class="brand">KRV</div><div class="tagline">Logistics &amp; Heavy Machinery</div></div>
  <ul class="lines">
    <li><span class="dot"></span>+1 555 0142 800</li>
    <li><span class="dot"></span>d.reyes@krvlogistics.com</li>
    <li><span class="dot"></span>www.krvlogistics.com</li>
  </ul>
  <div class="address">12 Harbor Road, Suite 4<br>Port City, 00000</div>
  <div class="base"></div>
</section>

<!-- business card back -->
<section class="piece card-back" aria-label="Business card back"><div class="brand">KRV</div></section>

<!-- letterhead with letter -->
<section class="piece letterhead first" aria-label="Letterhead">
  <svg class="wave" viewBox="0 0 326 70" preserveAspectRatio="none" height="70">
    <path d="M0 0H326V62C230 44 120 16 0 26Z" fill="var(--navy)"/>
    <path d="M0 31C120 21 230 49 326 68" stroke="var(--orange)" stroke-width="2.5" fill="none"/>
  </svg>
  <div class="contact-white">12 Harbor Road, Port City<br>+1 555 0142 800<br>info@krvlogistics.com<br>www.krvlogistics.com</div>
  <div class="brand-block"><div class="brand">KRV</div><div class="tagline">Logistics &amp; Heavy Machinery</div></div>
  <div class="letter-body">
    <div class="salutation">Dear Mr. Harlow,</div>
    <p class="tiny">Thank you for choosing our team for your upcoming project. We are pleased to confirm the transport schedule, crane support and site delivery plan discussed during our recent meeting at your office.</p>
    <p class="tiny">Our fleet will arrive on the agreed date with trained operators, full insurance cover and safety equipment. Each stage of the move will be tracked and reported to your project manager every day.</p>
    <p class="tiny">Please review the attached quotation and timeline. Should you need any changes, our coordinators are ready to adjust the plan so that every load reaches its destination on time.</p>
    <svg class="signature" viewBox="0 0 40 10"><path d="M1 8C5 1 8 1 9 7S14 2 17 6 22 3 25 7 31 2 39 5" stroke="#333" stroke-width=".8" fill="none"/></svg>
    <p class="tiny">Sincerely,</p>
  </div>
</section>

<!-- letterhead blank -->
<section class="piece letterhead second" aria-label="Letterhead second sheet">
  <svg class="wave" viewBox="0 0 326 70" preserveAspectRatio="none" height="70">
    <path d="M0 0H326V62C230 44 120 16 0 26Z" fill="var(--navy)"/>
    <path d="M0 31C120 21 230 49 326 68" stroke="var(--orange)" stroke-width="2.5" fill="none"/>
  </svg>
  <div class="contact-white">12 Harbor Road, Port City<br>+1 555 0142 800<br>info@krvlogistics.com<br>www.krvlogistics.com</div>
  <div class="brand-block"><div class="brand">KRV</div><div class="tagline">Logistics &amp; Heavy Machinery</div></div>
  <div class="ruled"></div>
</section>

<!-- folder open -->
<section class="piece folder-open" aria-label="Presentation folder open">
  <div class="panel-left"><div class="brand">KRV</div></div>
  <svg class="wave" viewBox="0 0 326 40" preserveAspectRatio="none" height="40">
    <path d="M0 0H326V6C230 30 120 8 0 26Z" fill="var(--paper)"/>
  </svg>
  <div class="fold"></div>
  <div class="sheet">
    <p class="tiny">Thank you for choosing our team for your upcoming project. We confirm the transport schedule and delivery plan.</p>
    <p class="tiny">Our fleet will arrive on the agreed date with trained operators and full safety equipment for every load.</p>
    <p class="tiny">Sincerely,</p>
  </div>
</section>

<!-- folder closed -->
<section class="piece folder-closed" aria-label="Presentation folder closed">
  <div class="insert"><div class="brand">KRV</div><p class="tiny">Project overview, fleet details and delivery terms.</p></div>
  <svg class="flap" viewBox="0 0 326 253" preserveAspectRatio="none">
    <path d="M0 130C120 100 220 120 326 96V253H0Z" fill="var(--navy)"/>
    <path d="M0 126C120 96 220 116 326 92" stroke="var(--orange)" stroke-width="2" fill="none"/>
    <path d="M70 253V200" stroke="var(--navy-deep)" stroke-width="2"/>
  </svg>
</section>

<!-- envelope front -->
<section class="piece envelope env-front" aria-label="Envelope front">
  <svg class="wave" viewBox="0 0 330 40" preserveAspectRatio="none" height="40">
    <path d="M0 0H330V34C230 22 120 6 0 14Z" fill="var(--navy)"/>
    <path d="M0 18C120 10 230 26 330 38" stroke="var(--orange)" stroke-width="2" fill="none"/>
  </svg>
  <div class="brand-block"><div class="brand">KRV</div><div class="tagline">Logistics &amp; Heavy Machinery</div></div>
</section>

<!-- envelope back white -->
<section class="piece envelope env-back" aria-label="Envelope back">
  <svg class="flap" viewBox="0 0 330 125" preserveAspectRatio="none">
    <path d="M0 0L150 48H180L330 0" stroke="#cfd3d6" stroke-width="1" fill="none"/>
  </svg>
  <div class="brand">KRV</div>
</section>

<!-- envelope back navy -->
<section class="piece envelope env-back-navy" aria-label="Envelope back navy">
  <svg class="flap" viewBox="0 0 330 133" preserveAspectRatio="none">
    <path d="M0 0L150 50H180L330 0" stroke="var(--navy-deep)" stroke-width="1.5" fill="none"/>
  </svg>
  <div class="brand">KRV</div>
</section>

</body>
</html>
```